Redesign a Start-Up Dating Website

Website: https://morvelink.com.
Make sure the design has an island style theme.
I would like the 7 pages of my website to have a new and professional look. I want the same colors to remain, but I want a creative look for all the pages. This is a dating website that is in the startup stage. So, I want to give my entire website a custom makeover. I want something that will stand out from the other dating sites. Something that will attract more people to want to use my services, and hopefully get new members.
Target Market(s)
Dating
Industry/Entity Type
Dating
Coding
Coded - Design and coding required
Number of Pages Required
5+ page
Font styles to use
Other font styles liked:
- Decorative, San Serif
Requirements
Must have
- The design must have the original colors and a stylish font to go along. The design must be creative, welcoming, and professional. I would like an island style theme for the website. This is a dating website so make sure that the design is tailored to that aspect.
Nice to have
- It would be nice to have a decorative font and a professional style on all the pages. Make sure the design will be mobile responsive and friendly for all the pages on the website.
Should not have
- The design should not be bland and uncreative.

```html
<!DOCTYPE html>
<html lang="en">
<head>
<meta charset="utf-8">
<title>Morvelink – Online Dating Made Easy</title>
<link href="https://fonts.googleapis.com/css2?family=Raleway:wght@400;600;700;800;900&family=Open+Sans:wght@400;600;700&display=swap" rel="stylesheet">
<style>
:root{
  --teal:#27b3a2;
  --teal-dark:#1c8f82;
  --orange:#f4a11c;
  --orange-dark:#e48a0c;
  --purple:#6b3f9b;
  --purple-dark:#54297f;
  --footer:#0f4a3a;
  --footer-dark:#0a3a2d;
  --ink:#4a4a4a;
  --muted:#8a8a8a;
  --white:#ffffff;
  --line:#e3e3e3;
}
*{box-sizing:border-box;margin:0;padding:0}
html,body{width:1200px;height:2520px;overflow:hidden}
body{font-family:"Open Sans",Arial,sans-serif;color:var(--ink);background:var(--white);position:relative}
.display{font-family:"Raleway","Open Sans",sans-serif}

/* HERO */
.hero{position:relative;height:560px;overflow:hidden}
.hero-photo{position:absolute;inset:0;background:
  radial-gradient(ellipse at 72% 30%,#e8c7a6 0%,rgba(232,199,166,0) 30%),
  radial-gradient(ellipse at 30% 10%,#eef3e6 0%,rgba(238,243,230,0) 45%),
  linear-gradient(180deg,#c9d8b8 0%,#8fae6a 45%,#5f8a3d 75%,#486d2c 100%)}
.brand{position:absolute;top:42px;left:0;right:0;display:flex;flex-direction:column;align-items:center;gap:8px}
.brand-mark{width:58px;height:58px;border-radius:50%;background:var(--orange);border:4px solid var(--white)}
.brand-name{font-family:"Raleway",sans-serif;font-weight:800;font-size:30px;color:var(--white);letter-spacing:.5px}
.hero-tag{position:absolute;left:160px;top:254px;color:var(--white)}
.hero-tag small{display:block;font-size:17px;letter-spacing:1px;font-weight:600}
.hero-tag strong{display:block;font-family:"Raleway",sans-serif;font-weight:900;font-size:44px;line-height:1.05}
.hero-search{position:absolute;right:170px;top:290px;display:flex}
.hero-search span{width:150px;height:28px;background:var(--white);border-radius:3px 0 0 3px;font-size:12px;color:var(--muted);padding:6px 10px}
.hero-search i{width:30px;height:28px;background:var(--orange);border-radius:0 3px 3px 0}
.nav{position:absolute;left:160px;right:160px;top:340px;height:32px;background:var(--teal);display:flex;align-items:center;padding:0 18px}
.nav a{color:var(--white);text-decoration:none;font-size:12px;font-weight:600;margin-right:34px}
.nav .social{margin-left:auto;display:flex;gap:10px}
.nav .social i{width:12px;height:12px;border-radius:50%;background:var(--white);opacity:.9}
.banner{position:absolute;left:160px;right:160px;top:384px;height:160px;background:rgba(244,161,28,.9);text-align:center;padding-top:18px}
.banner h1{font-family:"Raleway",sans-serif;font-weight:900;font-size:40px;color:var(--purple);letter-spacing:.5px}
.banner p{color:var(--white);font-size:13px;width:640px;margin:10px auto 0;line-height:1.5}
.btn{display:inline-flex;align-items:center;gap:8px;border-radius:3px;color:var(--white);font-weight:700;font-size:12px;text-decoration:none}
.btn-join{background:var(--purple);padding:9px 20px;margin-top:12px}

/* WELCOME */
.welcome{height:640px;padding-top:46px;text-align:center}
.welcome h2{font-family:"Raleway",sans-serif;font-weight:800;font-size:48px;color:var(--teal);letter-spacing:1px}
.welcome .sub{font-family:"Raleway",sans-serif;font-weight:700;font-size:24px;color:var(--muted)}
.welcome .intro{width:880px;margin:22px auto 0;font-size:13px;line-height:1.7;color:var(--muted)}
.welcome-body{display:flex;gap:40px;width:880px;margin:40px auto 0;text-align:left}
.tiles{display:grid;grid-template-columns:repeat(2,190px);gap:10px}
.tile{position:relative;height:160px}
.tile-photo{position:absolute;inset:0}
.tile-label{position:absolute;left:10px;bottom:10px;color:var(--white);font-weight:700;font-size:12px;line-height:1.3}
.signup{flex:1;border:4px solid var(--purple);padding:26px 30px;height:300px}
.signup h3{text-align:center;font-size:12px;color:var(--muted);font-weight:600}
.signup h4{text-align:center;font-family:"Raleway",sans-serif;font-weight:800;font-size:24px;color:var(--purple);margin-bottom:20px}
.row{display:flex;gap:12px;margin-bottom:12px;align-items:center}
.field{flex:1;height:32px;border:1px solid var(--line);font-size:12px;color:var(--muted);padding:7px 10px}
.field.tall{height:56px}
.radio{display:flex;gap:6px;align-items:center;font-size:12px;color:var(--muted)}
.radio i{width:11px;height:11px;border:1px solid var(--muted);border-radius:50%}
.btn-search{background:var(--orange);padding:7px 18px}

/* PROFILES */
.profiles{height:350px;position:relative}
.ribbon{position:absolute;left:0;right:0;top:0;height:76px}
.ribbon-bar{position:absolute;left:330px;right:330px;top:0;height:76px;background:var(--teal);text-align:center;color:var(--white);padding-top:10px}
.ribbon-bar h2{font-family:"Raleway",sans-serif;font-weight:800;font-size:32px;line-height:1}
.ribbon-bar p{font-size:14px;margin-top:6px}
.ribbon svg{position:absolute;left:0;top:0}
.profile-list{position:absolute;top:110px;left:160px;right:160px;display:flex;justify-content:space-around}
.profile{text-align:center;width:200px}
.avatar{width:150px;height:150px;border-radius:50%;border:6px solid var(--teal);margin:0 auto;background:radial-gradient(circle at 50% 40%,#d9b394,#8a6a55)}
.profile h5{color:var(--orange);font-family:"Raleway",sans-serif;font-weight:800;font-size:18px;margin-top:14px}
.profile p{font-size:12px;color:var(--muted)}

/* TRIAL BAND */
.trial{height:90px;background:var(--purple);display:flex;align-items:center;padding:0 160px;color:var(--white)}
.trial-icon{width:52px;height:52px;border-radius:50%;border:3px solid var(--white);display:flex;align-items:center;justify-content:center;margin-right:18px}
.trial h3{font-family:"Raleway",sans-serif;font-weight:800;font-size:27px}
.trial p{font-size:12px;opacity:.85}
.btn-trial{margin-left:auto;background:var(--teal);padding:10px 18px}

/* FEATURES */
.features{height:520px;text-align:center;padding-top:32px}
.features h2{font-family:"Raleway",sans-serif;font-weight:800;font-size:36px;color:var(--teal)}
.features h2 span{color:var(--orange)}
.features h3{font-family:"Raleway",sans-serif;font-weight:900;font-size:64px;color:var(--orange);line-height:1;letter-spacing:2px}
.cards{display:flex;gap:40px;justify-content:center;margin-top:36px}
.card{width:240px;height:320px;color:var(--white);padding:30px 22px}
.card.orange{background:var(--orange)}
.card.teal{background:var(--teal)}
.card.purple{background:var(--purple)}
.card-icon{width:120px;height:110px;margin:0 auto;border:3px solid var(--white);border-radius:6px;display:flex;align-items:center;justify-content:center}
.card h4{font-family:"Raleway",sans-serif;font-weight:800;font-size:19px;margin-top:24px}
.card p{font-size:12px;line-height:1.5;margin-top:10px;opacity:.95}
.card .more{display:inline-block;margin-top:10px}

/* FOOTER */
.footer{position:absolute;left:0;right:0;top:2160px;height:360px;background:var(--footer);color:var(--white)}
.footer-nav{display:flex;justify-content:center;gap:70px;height:40px;align-items:center;border-bottom:1px solid rgba(255,255,255,.15);font-size:11px;font-weight:600}
.footer-cols{display:flex;gap:60px;padding:34px 160px 0}
.footer-about{width:240px}
.footer-logo{width:170px;height:90px;background:var(--white);display:flex;align-items:center;justify-content:center;gap:8px}
.footer-logo i{width:22px;height:22px;border-radius:50%;background:var(--orange)}
.footer-logo b{font-family:"Raleway",sans-serif;font-weight:800;font-size:22px;color:var(--teal)}
.footer-about p{font-size:11px;line-height:1.5;opacity:.8;margin-top:12px}
.footer-social{display:flex;gap:10px;margin-top:12px}
.footer-social i{width:24px;height:24px;border-radius:50%;background:var(--white);opacity:.9}
.footer h6{font-size:13px;font-weight:700;margin-bottom:16px;letter-spacing:.5px}
.contact{width:260px}
.contact li{list-style:none;display:flex;gap:10px;align-items:center;font-size:12px;margin-bottom:14px;opacity:.9}
.mailing{flex:1}
.mailing p{font-size:11px;opacity:.8;line-height:1.5}
.mail-field{height:30px;background:var(--white);color:var(--muted);font-size:12px;padding:6px 10px;margin-top:14px}
.btn-sub{background:var(--purple);padding:7px 16px;margin-top:10px}
.copyright{position:absolute;left:0;right:0;bottom:0;height:40px;background:var(--footer-dark);text-align:center;font-size:11px;line-height:40px;opacity:.9}
</style>
</head>
<body>

<header class="hero">
  <div class="hero-photo" role="img" aria-label="Photo of a smiling couple embracing outdoors in a green summer meadow"></div>
  <div class="brand">
    <span class="brand-mark"></span>
    <span class="brand-name">Morvelink</span>
  </div>
  <div class="hero-tag">
    <small>ONLINE DATING MADE EASY ON</small>
    <strong>MORVELINK.COM</strong>
  </div>
  <div class="hero-search"><span>Search...</span><i></i></div>
  <nav class="nav">
    <a href="#">HOME</a><a href="#">SEARCH</a><a href="#">MEMBERS</a><a href="#">EVENTS</a><a href="#">ABOUT</a><a href="#">PREMIUM</a><a href="#">CONTACT</a>
    <span class="social"><i></i><i></i><i></i><i></i></span>
  </nav>
  <section class="banner">
    <h1>FIND YOUR PERFECT MATCH FOR FREE!</h1>
    <p>Meet genuine singles near you, chat freely and plan your first island date today. Joining takes a minute and costs nothing at all.</p>
    <a class="btn btn-join" href="#">
      <svg width="12" height="12" viewBox="0 0 12 12"><path d="M6 11 1.5 6.5A2.6 2.6 0 0 1 6 3a2.6 2.6 0 0 1 4.5 3.5Z" fill="#fff"/></svg>JOIN NOW</a>
  </section>
</header>

<section class="welcome">
  <h2>WELCOME TO</h2>
  <p class="sub">Dating is EASY with Morvelink</p>
  <p class="intro">Morvelink brings together warm, honest people who want real connection. Browse profiles, send a message and discover who shares your love of sunsets, beaches and long conversations. Our friendly community grows every day, and every member is verified so you can date with confidence and ease. Start your story here and let the island breeze guide you.</p>
  <div class="welcome-body">
    <div class="tiles">
      <div class="tile"><div class="tile-photo" role="img" aria-label="Member portrait photo" style="background:linear-gradient(160deg,#b98a7a,#6d4a58)"></div><span class="tile-label">LENA<br>GERMANY</span></div>
      <div class="tile"><div class="tile-photo" role="img" aria-label="Member portrait photo" style="background:linear-gradient(160deg,#8b6f60,#3e2f2c)"></div><span class="tile-label">CLAIRE<br>UNITED STATES</span></div>
      <div class="tile"><div class="tile-photo" role="img" aria-label="Member portrait photo" style="background:linear-gradient(160deg,#9a7bb0,#4b2f63)"></div><span class="tile-label">UNITED STATES</span></div>
      <div class="tile"><div class="tile-photo" role="img" aria-label="Member portrait photo" style="background:linear-gradient(160deg,#9c8a7c,#4d3f38)"></div><span class="tile-label">CANADA</span></div>
    </div>
    <form class="signup">
      <h3>JOIN OUR COMMUNITY OF</h3>
      <h4>1 MORVELINK MEMBERS</h4>
      <div class="row"><span class="field">First Name</span><span class="field">Last Name</span></div>
      <div class="row"><span class="field">Email</span><span class="radio"><i></i>Man</span><span class="radio"><i></i>Woman</span></div>
      <div class="row"><span class="field tall">Message</span></div>
      <a class="btn btn-search" href="#">SEARCH</a>
    </form>
  </div>
</section>

<section class="profiles">
  <div class="ribbon">
    <svg width="1200" height="76" viewBox="0 0 1200 76" aria-hidden="true">
      <path d="M160 38 H330" stroke="var(--teal)" stroke-width="3"/>
      <path d="M870 38 H1040" stroke="var(--teal)" stroke-width="3"/>
    </svg>
    <div class="ribbon-bar"><h2>LAST ADDED PROFILES</h2><p>your search for love and companionship ends here!</p></div>
  </div>
  <div class="profile-list">
    <div class="profile"><div class="avatar" role="img" aria-label="Profile photo of Lena"></div><h5>LENA</h5><p>Age 27, Toronto</p></div>
    <div class="profile"><div class="avatar" role="img" aria-label="Profile photo of Tobias"></div><h5>TOBIAS</h5><p>Age 31, Berlin</p></div>
    <div class="profile"><div class="avatar" role="img" aria-label="Profile photo of Sienna"></div><h5>SIENNA</h5><p>Age 25, Miami</p></div>
    <div class="profile"><div class="avatar" role="img" aria-label="Profile photo of Julian"></div><h5>JULIAN</h5><p>Age 34, Sydney</p></div>
  </div>
</section>

<section class="trial">
  <span class="trial-icon"><svg width="22" height="22" viewBox="0 0 22 22"><path d="M4 11l5 5 9-10" stroke="#fff" stroke-width="3" fill="none"/></svg></span>
  <div><h3>SIGN-UP FOR A 30 DAYS FREE TRIAL</h3><p>Enjoy all the benefits of a premium membership with no commitment.</p></div>
  <a class="btn btn-trial" href="#">Start Morvelink with Free Sign Up</a>
</section>

<section class="features">
  <h2><span>100%</span> COMPLETELY FREE DATING IN</h2>
  <h3>MORVELINK</h3>
  <div class="cards">
    <div class="card orange">
      <div class="card-icon"><svg width="56" height="56" viewBox="0 0 56 56"><circle cx="28" cy="20" r="10" fill="none" stroke="#fff" stroke-width="4"/><path d="M10 50c2-12 10-16 18-16s16 4 18 16" fill="none" stroke="#fff" stroke-width="4"/></svg></div>
      <h4>CREATE A PROFILE</h4>
      <p>Tell others about yourself, add your best photos and share what makes you smile.</p>
      <span class="more">&rarr;</span>
    </div>
    <div class="card teal">
      <div class="card-icon"><svg width="56" height="56" viewBox="0 0 56 56"><circle cx="24" cy="24" r="14" fill="none" stroke="#fff" stroke-width="4"/><path d="M34 34l14 14" stroke="#fff" stroke-width="5"/></svg></div>
      <h4>FIND MATCHES</h4>
      <p>Search by age, place and interests to discover singles who suit you perfectly.</p>
      <span class="more">&rarr;</span>
    </div>
    <div class="card purple">
      <div class="card-icon"><svg width="56" height="56" viewBox="0 0 56 56"><path d="M28 48 8 28A11 11 0 0 1 28 13a11 11 0 0 1 20 15Z" fill="none" stroke="#fff" stroke-width="4"/></svg></div>
      <h4>START DATING</h4>
      <p>Send a message, plan a meeting and enjoy your very first date by the sea.</p>
      <span class="more">&rarr;</span>
    </div>
  </div>
</section>

<footer class="footer">
  <nav class="footer-nav"><span>HOME</span><span>SEARCH</span><span>MEMBERS</span><span>EVENTS</span><span>ABOUT</span><span>PREMIUM</span><span>CONTACT</span></nav>
  <div class="footer-cols">
    <div class="footer-about">
      <div class="footer-logo"><i></i><b>Morvelink</b></div>
      <p>Find love on the island of singles, where every member is one smile away.</p>
      <div class="footer-social"><i></i><i></i><i></i><i></i></div>
    </div>
    <div class="contact">
      <h6>CONTACT INFORMATION</h6>
      <ul>
        <li><svg width="14" height="16" viewBox="0 0 14 16"><path d="M7 15S1 9 1 6a6 6 0 0 1 12 0c0 3-6 9-6 9Z" fill="#fff"/><circle cx="7" cy="6" r="2" fill="var(--footer)"/></svg>14 Coral Bay Road, Palm Harbour</li>
        <li><svg width="14" height="14" viewBox="0 0 14 14"><path d="M3 1l3 3-2 2a8 8 0 0 0 4 4l2-2 3 3-2 2C5 13 1 9 1 3Z" fill="#fff"/></svg>1800 55 0192</li>
        <li><svg width="16" height="12" viewBox="0 0 16 12"><rect x="1" y="1" width="14" height="10" fill="none" stroke="#fff" stroke-width="1.6"/><path d="M1 1l7 6 7-6" fill="none" stroke="#fff" stroke-width="1.6"/></svg>contact@morvelink.com</li>
      </ul>
    </div>
    <div class="mailing">
      <h6>JOIN OUR MAILING LIST</h6>
      <p>Subscribe to receive news, events and dating tips straight to your inbox.</p>
      <div class="mail-field">Your email address</div>
      <a class="btn btn-sub" href="#">SUBSCRIBE</a>
    </div>
  </div>
  <div class="copyright">© 2017 morvelink.com. All Rights Reserved</div>
</footer>

</body>
</html>
```